Financial PR company Homepage and Inner Page design

Please design a web homepage and innerpage for OVIN Public Relations.
OVIN Public Relations is a Financial PR company targeting Shenzhen Qian Special Economical Zone.
Note:
1. Menu includes ( Please specialize in Chinese and we want to see the Chinese fonts)
关于我们/服务板块/专业优势/合作伙伴/前海商圈/公司新闻/加盟我们/联系我们

2. Please refer to world class PR Business company and contribute your idea on website design and color themes.

3. We have attached the Logo for reference.

4. Anytime use picture for reference, please select asian business people pictures.

Cheers,

HI Designers, Thanks for the design submission. Here is our client feedback: 1. Adopt one screen design. 2. Use amiable Asia Business woman pictures. 3. Use contrastive color theme for the design. Cheers, Kip From TW

```html
<!DOCTYPE html>
<html lang="zh-CN">
<head>
<meta charset="utf-8">
<title>OVIN PR</title>
<link rel="stylesheet" href="https://fonts.googleapis.com/css2?family=Arimo:wght@400;700&family=Mulish:wght@400;600&family=Noto+Sans+SC:wght@500;700&family=PT+Sans:wght@400;700&family=Questrial&display=swap">
<style>
  :root {
    --sky: #22a7e0;
    --sky-light: #5cb6e6;
    --ink: #111111;
    --body-text: #4d4d4d;
    --heading-grey: #6a6a6a;
    --heading-blue: #1f6db5;
    --teal: #1d5e7c;
    --link: #1b8fd0;
    --rule: #9a9a9a;
    --paper: #ffffff;
    --mist: #e9e9e9;
    --bullet: #4a4a4a;
    --side-heading: #0f2b3a;
  }
  * { margin: 0; padding: 0; box-sizing: border-box; }
  html, body { width: 1200px; height: 881px; overflow: hidden; }
  body {
    position: relative;
    background: linear-gradient(to bottom, var(--mist) 0, var(--mist) 419px, #f6f6f6 470px, var(--paper) 620px);
    font-family: "Arimo", Arial, sans-serif;
    color: var(--body-text);
  }
  .abs { position: absolute; }

  /* sidebar */
  .sidebar { left: 127px; top: 0; width: 220px; height: 777px; background: var(--sky); }
  .brand { left: 0; top: 0; width: 220px; height: 100px; background: var(--paper);
    display: flex; align-items: center; justify-content: center; gap: 10px; }
  .brand-dot { width: 38px; height: 38px; border-radius: 50%; background: var(--sky-light); }
  .brand-name { font-family: "Mulish", sans-serif; font-weight: 400; font-size: 30px; color: var(--sky-light); letter-spacing: 0.5px; }
  .nav { left: 0; top: 100px; width: 220px; list-style: none;
    font-family: "Noto Sans SC", sans-serif; font-weight: 700; font-size: 14px; color: var(--paper); }
  .nav li { height: 29px; line-height: 29px; padding-left: 17px; }
  .nav li.current { background: var(--ink); height: 34px; line-height: 34px; }
  .side-title { left: 17px; font-family: "PT Sans", sans-serif; font-weight: 400; font-size: 20px; color: var(--side-heading); }
  .side-rule { left: 0; width: 220px; border-top: 1px dashed rgba(255,255,255,0.85); }
  .side-contact { left: 17px; top: 477px; font-family: "PT Sans", sans-serif; font-size: 13px; line-height: 19px; color: var(--paper); }
  .signup { left: 18px; top: 614px; width: 187px; height: 28px; background: var(--paper); border: 1px solid #cfcfcf; }
  .signup span { position: absolute; left: 9px; top: 8px; font-family: "PT Sans", sans-serif; font-size: 9px; color: #333; }
  .signup b { position: absolute; right: 2px; top: 2px; width: 54px; height: 22px; background: var(--ink); color: var(--paper);
    font-family: "PT Sans", sans-serif; font-size: 10px; line-height: 22px; text-align: center; }
  .social { top: 713px; width: 26px; height: 26px; border-radius: 5px; background: #e6f5fc; }

  /* hero */
  .hero-photo { left: 347px; top: 0; width: 853px; height: 419px;
    background: linear-gradient(100deg, #e4e4e4 0%, #efefef 40%, #f4f3f1 65%, #d8c2b0 85%, #8a5a3e 100%); }
  .hero-caption { left: 347px; top: 316px; width: 523px; height: 103px; background: rgba(255,255,255,0.93); }
  .hero-caption h2 { position: absolute; left: 23px; top: 18px; font-family: "Mulish", sans-serif; font-weight: 400; font-size: 24px; color: var(--ink); }
  .hero-caption p { position: absolute; left: 23px; top: 51px; font-family: "Mulish", sans-serif; font-size: 24px; color: var(--teal); }
  .top-contact { left: 898px; top: 17px; width: 148px; height: 58px; background: rgba(255,255,255,0.55);
    font-family: "Arimo", sans-serif; font-size: 12px; color: var(--heading-blue); }
  .top-contact div { position: absolute; left: 7px; display: flex; align-items: center; gap: 10px; }

  /* content */
  .welcome { left: 377px; top: 433px; font-family: "Questrial", sans-serif; font-size: 28px; color: var(--heading-grey); font-weight: 700; }
  .welcome em { font-style: normal; color: var(--sky-light); font-weight: 400; }
  .copy { font-size: 12.5px; line-height: 19.4px; color: var(--body-text); }
  .more { font-family: "PT Sans", sans-serif; font-size: 13px; color: var(--link); }
  .dots { left: 379px; top: 578px; width: 667px; border-top: 1px dotted #555; }
  .section-title { font-family: "Arimo", sans-serif; font-weight: 700; font-size: 19.5px; color: var(--heading-blue); }
  .reasons { list-style: none; font-size: 13px; color: #333; }
  .reasons li { height: 22.3px; display: flex; align-items: center; gap: 8px; }
  .reasons li::before { content: ""; width: 14px; height: 14px; border-radius: 50%; background: var(--bullet);
    background-image: linear-gradient(45deg, transparent 45%, #fff 45%, #fff 55%, transparent 55%), linear-gradient(-45deg, transparent 45%, #fff 45%, #fff 55%, transparent 55%);
    background-size: 6px 6px, 6px 6px; background-position: 5px 4px, 5px 7px; background-repeat: no-repeat; flex: none; }

  /* footer */
  .footer-rule { left: 130px; top: 806px; width: 940px; height: 4px; background: var(--rule); }
  .footer-links { left: 135px; top: 826px; font-family: "Mulish", sans-serif; font-size: 12.5px; color: #555; }
  .footer-links i { font-style: normal; margin: 0 9px; color: #888; font-size: 10px; }
  .copyright { left: 135px; top: 848px; font-family: "Mulish", sans-serif; font-size: 12px; color: #555; }
  .footer-brand { left: 893px; top: 820px; display: flex; align-items: center; gap: 10px; }
  .footer-brand .brand-dot { width: 34px; height: 34px; }
  .footer-brand .brand-name { font-size: 28px; }
</style>
</head>
<body>

  <div class="abs hero-photo" role="img" aria-label="Photo of a smiling Asian businesswoman drawing a rising red arrow on a bar chart"></div>

  <div class="abs top-contact">
    <div style="top:9px">
      <svg width="20" height="13" viewBox="0 0 20 13"><rect x="0.5" y="0.5" width="19" height="12" fill="none" stroke="#1f6db5"/><path d="M0.5 0.5 L10 7 L19.5 0.5" fill="none" stroke="#1f6db5"/></svg>
      <span>mail@ovinpr.com</span>
    </div>
    <div style="top:34px">
      <svg width="20" height="14" viewBox="0 0 20 14"><path d="M1 5 Q10 -1 19 5 L16 7 L14 5 L6 5 L4 7 Z" fill="#1f6db5"/><rect x="4" y="7" width="12" height="7" rx="1" fill="#1f6db5"/><circle cx="10" cy="10.5" r="2" fill="#fff"/></svg>
      <span>800 555 01234</span>
    </div>
  </div>

  <div class="abs hero-caption">
    <h2>Our Company Core Values</h2>
    <p>Integrity, Courage, Innovation, Execution</p>
  </div>

  <aside class="abs sidebar">
    <div class="abs brand"><span class="brand-dot"></span><span class="brand-name">OVIN PR</span></div>
    <ul class="abs nav">
      <li class="current">首页</li>
      <li>关于我们</li>
      <li>服务板块</li>
      <li>专业优势</li>
      <li>合作伙伴</li>
      <li>前海商圈</li>
      <li>公司新闻</li>
      <li>加盟我们</li>
      <li>联系我们</li>
    </ul>

    <h3 class="abs side-title" style="top:424px">Contact</h3>
    <div class="abs side-rule" style="top:460px"></div>
    <div class="abs side-contact">OVIN.com<br>800-555-01234<br>support@OVIN.com</div>
    <div class="abs side-rule" style="top:554px"></div>
    <h3 class="abs side-title" style="top:580px">Subscribe Newsletter</h3>
    <div class="abs signup"><span>enter your e-mail address</span><b>Sign Up!</b></div>
    <div class="abs side-rule" style="top:666px"></div>
    <h3 class="abs side-title" style="top:682px">Find Us On</h3>
    <span class="abs social" style="left:18px"></span>
    <span class="abs social" style="left:54px"></span>
    <span class="abs social" style="left:89px"></span>
  </aside>

  <main>
    <h1 class="abs welcome">Welcome To <em>OVIN PR</em></h1>
    <p class="abs copy" style="left:377px; top:470px; width:690px">Lorem Ipsum is simply dummy text of the printing and typesetting industry. Lorem Ipsum has been the industry's standard dummy text ever since the 1500s, when an unknown printer took a galley of type and scrambled it to make a type specimen book. It has survived not only five centuries,</p>
    <a class="abs more" style="left:377px; top:534px">Read more &gt;</a>

    <div class="abs dots"></div>

    <h2 class="abs section-title" style="left:379px; top:603px">What We Do</h2>
    <p class="abs copy" style="left:379px; top:631px; width:315px">Lorem Ipsum is simply dummy text of the printing and typesetting industry. Lorem Ipsum has been the industry's standard dummy text ever since the 1500s, when an unknown printer took a galley of type and scrambled it to make a type specimen book.</p>
    <a class="abs more" style="left:377px; top:737px">Read more &gt;</a>

    <h2 class="abs section-title" style="left:736px; top:601px">Why Choose Us</h2>
    <ul class="abs reasons" style="left:742px; top:631px">
      <li>Be Proactive</li><li>Be Responsive</li><li>Be Honest</li><li>Position yourself</li><li>Manage Expectations</li>
    </ul>
    <ul class="abs reasons" style="left:910px; top:631px">
      <li>Be Proactive</li><li>Be Responsive</li><li>Be Honest</li><li>Position yourself</li><li>Manage Expectations</li>
    </ul>
  </main>

  <footer>
    <div class="abs footer-rule"></div>
    <nav class="abs footer-links">Home<i>|</i>About Us<i>|</i>Services<i>|</i>Careers<i>|</i>Contact Us</nav>
    <p class="abs copyright">Copyright © OVIN PR 2014 All Rights Reserved</p>
    <div class="abs footer-brand"><span class="brand-dot"></span><span class="brand-name">OVIN PR</span></div>
  </footer>

</body>
</html>
```